Harbor Nest Lodging website, brand new company, that rents rooms out in houses to milleniuls

We have a site right now that is weak as heck! We could use some punching it up. So we want it to be fun and cool, with added items in for social media (just chirpnet now) and anything else you want to throw at us. We do have a “blog” in there dedicated to events (we throw a lot of them) so want to incorporate that. Also have an existing design for a hand out that we want to use as our launching pad for colors… you can deviate from it a bit though.

Target Market(s)

25-40 year olds transitioning to the city from other places in the country. Millennial are the min group

Industry/Entity Type

Real Estate

Coding

Coded - Design and coding required

Number of Pages Required

5+ page

Font styles to use
Sans Serif

Requirements
Must have
• Fun look, same pages as those uploaded, but not necessarily the look and feel of what we have already.
• Follow the content of our posted site www.HarborNestLodging.example
• FOOTER
• LOGO | SITEMAP | SOCIAL LINKS | MAIN CTA REMINDER | CONTACT INFO | COPYRIGHT INFO | TERMS AND CONDITIONS
Nice to have
• Use as many of my graphics as loaded, but feel free to use stock photos as well interlaced. Including both people in their 20’s, 30’s, 40’s, having a fun time or of nice houses, inside and out.

```html
<!DOCTYPE html>
<html lang="en">
<head>
<meta charset="utf-8">
<title>Harbor Nest Lodging</title>
<link href="https://fonts.googleapis.com/css2?family=Raleway:wght@500;600;700&family=Open+Sans:wght@400;600;700&family=Dancing+Script&display=swap" rel="stylesheet">
<style>
:root{
  --blue:#1565c0;
  --blue-deep:#0d4fa8;
  --ink:#333;
  --rule:#cfcfcf;
  --light:#f3f3f3;
  --footer:#2a2a2a;
  --nav-active:#6b6b6b;
}
*{margin:0;padding:0;box-sizing:border-box}
html,body{width:682px;height:1200px;overflow:hidden;background:#fff}
body{font-family:"Open Sans",sans-serif;color:var(--ink);position:relative}

/* header */
.header{position:absolute;top:0;left:0;width:682px;height:60px;background:linear-gradient(#fff,#eef3fa)}
.call{position:absolute;left:91px;top:17px;display:flex;align-items:center;gap:5px}
.call small{display:block;font-size:7px}
.call strong{display:block;font-size:10px;font-weight:600;line-height:1}
.brand{position:absolute;left:0;width:682px;top:22px;text-align:center;font-family:"Raleway",sans-serif;font-weight:700;font-size:14px;color:var(--blue);letter-spacing:.5px;text-transform:uppercase}
.search{position:absolute;left:460px;top:19px;width:130px;height:19px;border:1px solid #ddd;background:#fff;font-size:6.5px;color:#999;padding:5px 6px}
.search svg{position:absolute;right:5px;top:5px}

/* nav */
.nav{position:absolute;top:61px;left:0;width:682px;height:26px;background:var(--blue);border-bottom:2px solid #fff;box-shadow:0 2px 0 var(--blue)}
.nav ul{list-style:none;display:flex;position:absolute;left:91px;top:0;height:26px}
.nav li{font-family:"Raleway",sans-serif;font-size:7.5px;font-weight:600;color:#fff;letter-spacing:.6px;padding:0 13.5px;line-height:26px}
.nav li.active{background:var(--nav-active);padding:0 16px}

/* photo fills */
.hero{position:absolute;top:91px;left:0;width:682px;height:257px;
  background:
    radial-gradient(ellipse 90px 50px at 405px 215px,rgba(205,45,70,.75),rgba(205,45,70,0)),
    radial-gradient(ellipse 70px 30px at 200px 200px,rgba(220,60,90,.5),rgba(220,60,90,0)),
    radial-gradient(ellipse 230px 160px at 560px 90px,#f4f6f4,rgba(244,246,244,0)),
    linear-gradient(180deg,rgba(0,0,0,0) 60%,rgba(150,70,25,.55) 100%),
    linear-gradient(100deg,#9a4a1e 0%,#d88a44 22%,#c47435 38%,#7a4a2c 52%,#c9d0d2 66%,#e9ecea 100%)}
.hero-caption{position:absolute;left:0;top:122px;width:382px;height:26px;background:rgba(40,40,40,.6);color:#fff;font-family:"Raleway",sans-serif;font-size:15px;font-weight:500;line-height:26px;padding-left:93px}
.hero-caption b{font-weight:700}
.hero-caption sub{font-size:5px;vertical-align:4px}
.hero-arrows{position:absolute;left:9px;top:129px}

/* heading */
.heading{font-family:"Raleway",sans-serif;font-weight:600;text-transform:uppercase;color:var(--ink);letter-spacing:.3px}
.heading span{color:var(--blue)}
.rule{height:1px;background:var(--rule);position:relative}
.rule::before{content:"";position:absolute;top:-1px;height:3px;width:25px;background:var(--blue)}
.rule.center::before{left:50%;margin-left:-12px}

/* welcome */
.welcome{position:absolute;top:348px;left:0;width:682px;height:166px;text-align:center}
.welcome .heading{margin-top:23px;font-size:13px}
.welcome .rule{width:275px;margin:8px auto 0}
.welcome p{width:445px;margin:20px auto 0;font-size:5.8px;line-height:11.4px;letter-spacing:-.05px}
.btn-primary{display:inline-block;margin-top:17px;background:var(--blue);color:#fff;font-family:"Raleway",sans-serif;font-weight:700;font-size:8px;padding:8px 12px;letter-spacing:.3px}

/* amenities */
.amenities{position:absolute;top:515px;left:0;width:682px;height:190px;background:linear-gradient(90deg,var(--blue-deep),var(--blue))}
.amenities .photo{position:absolute;left:0;top:0;width:290px;height:190px;
  background:
    radial-gradient(ellipse 18px 14px at 42px 95px,rgba(255,225,160,.9),rgba(255,225,160,0)),
    radial-gradient(ellipse 18px 14px at 205px 95px,rgba(255,225,160,.9),rgba(255,225,160,0)),
    radial-gradient(ellipse 110px 45px at 150px 165px,rgba(70,70,95,.75),rgba(70,70,95,0)),
    linear-gradient(90deg,#7f7466 0%,#b1a592 35%,#a59d8f 55%,#9fb3cf 80%,rgba(21,101,192,0) 100%)}
.amenities h2{position:absolute;left:289px;top:35px;color:#fff;font-family:"Raleway",sans-serif;font-weight:500;font-size:12.5px;letter-spacing:.3px}
.amenities h2 sup{font-size:6px}
.amenities .rule{position:absolute;left:289px;top:57px;width:197px;background:rgba(255,255,255,.6)}
.amenities .rule::before{background:#fff}
.amenities ul{position:absolute;top:71px;list-style:none;color:#e6eefa;font-size:7px}
.amenities li{display:flex;gap:5px;line-height:11px;margin-bottom:4.3px}
.amenities li svg{flex:none;margin-top:2px}
.list-a{left:292px}
.list-b{left:449px;width:140px}

/* columns */
.features{position:absolute;top:705px;left:91px;width:500px;height:246px;display:flex;justify-content:space-between}
.feature{width:153px}
.feature .heading{margin-top:22px;font-size:10.5px}
.feature .rule{margin-top:7px}
.feature .thumb{margin-top:14px;height:86px}
.feature p{margin-top:10px;font-size:5.6px;line-height:10.5px;letter-spacing:-.05px}
.btn-small{display:inline-flex;align-items:center;gap:2px;margin-top:8px;background:var(--blue);color:#fff;font-size:5.5px;font-weight:700;padding:5px 6px;border:1px solid #0a3f86}
.thumb-home{background:radial-gradient(ellipse 40px 20px at 70px 65px,rgba(190,120,130,.7),rgba(190,120,130,0)),radial-gradient(ellipse 60px 25px at 76px 18px,#eef0ea,rgba(238,240,234,0)),linear-gradient(180deg,#a86a45 0%,#d9c2a3 45%,#7a4a30 100%)}
.thumb-events{background:radial-gradient(ellipse 30px 25px at 40px 35px,rgba(230,190,160,.8),rgba(230,190,160,0)),radial-gradient(ellipse 30px 25px at 115px 35px,rgba(230,190,160,.8),rgba(230,190,160,0)),radial-gradient(ellipse 40px 15px at 76px 80px,rgba(240,225,180,.7),rgba(240,225,180,0)),linear-gradient(120deg,#3f3a36,#8a7d70 50%,#2f2b28)}
.thumb-addition{background:radial-gradient(ellipse 60px 25px at 80px 70px,rgba(80,100,160,.85),rgba(80,100,160,0)),radial-gradient(ellipse 14px 12px at 20px 40px,rgba(255,225,160,.9),rgba(255,225,160,0)),linear-gradient(180deg,#6e4a30 0%,#d5d0c4 40%,#8aa2b8 100%)}

/* fans */
.fans{position:absolute;top:951px;left:0;width:682px;height:197px;background:var(--light);border-top:1px solid #ddd;text-align:center}
.fans .heading{margin-top:22px;font-size:13px}
.fans .rule{width:190px;margin:7px auto 0}
.fan{position:absolute;top:72px;text-align:left}
.fan .avatar{position:absolute;left:0;top:0;width:80px;height:80px;border-radius:50%;border:3px solid #fff;box-shadow:0 0 0 1px #ccc}
.avatar-a{background:linear-gradient(180deg,#d9b98a 0%,#e6c9a6 50%,#3f5f9a 85%,#c83a3a 100%)}
.avatar-b{background:linear-gradient(180deg,#6b4a36 0%,#dcb79a 50%,#a98060 80%,#d9d2c8 100%)}
.fan blockquote{position:absolute;left:89px;top:-1px;width:146px;font-family:"Dancing Script",cursive;font-size:8px;line-height:12px;color:#444}
.fan .name{position:absolute;top:97px;width:80px;text-align:center;font-size:7.5px;font-weight:600;color:var(--blue);text-transform:uppercase}
.fan-a{left:94px}
.fan-b{left:358px}

/* footer */
.footer{position:absolute;top:1148px;left:0;width:682px;height:52px;background:var(--footer);color:#ddd}
.footer .brand-foot{position:absolute;left:91px;top:20px;width:95px;font-family:"Raleway",sans-serif;font-weight:700;font-size:8.5px;color:#fff;text-transform:uppercase;white-space:nowrap}
.footer address{position:absolute;left:194px;top:14px;font-style:normal;font-size:5.6px;line-height:10.5px}
.footer .social{position:absolute;left:520px;top:11px;display:flex;gap:4px}
.footer .social span{width:15px;height:15px;border:1px solid #fff;border-radius:50%}
.footer .copy{position:absolute;right:91px;top:37px;font-size:5.6px}
</style>
</head>
<body>

<header class="header">
  <div class="call">
    <svg width="19" height="19" viewBox="0 0 19 19" aria-hidden="true"><circle cx="9.5" cy="9.5" r="8.5" fill="none" stroke="#1565c0" stroke-width="1.2"/><path d="M7 5.5c-.8.4-1.2 1.2-.9 2.2.7 2.3 2.5 4.2 4.8 4.9 1 .3 1.8-.1 2.2-.9l-1.6-1.2-1 .8c-1-.5-1.8-1.3-2.3-2.3l.8-1z" fill="#1565c0"/></svg>
    <div><small>Call Us on</small><strong>000-555-0142</strong></div>
  </div>
  <div class="brand">Harbor Nest Lodging</div>
  <div class="search">Search
    <svg width="8" height="8" viewBox="0 0 8 8" aria-hidden="true"><circle cx="3.3" cy="3.3" r="2.5" fill="none" stroke="#888" stroke-width="1"/><path d="M5.2 5.2L7.5 7.5" stroke="#888" stroke-width="1"/></svg>
  </div>
</header>

<nav class="nav">
  <ul>
    <li class="active">WELCOME</li>
    <li>OUR COMMUNITIES</li>
    <li>AMMENITIES</li>
    <li>FITTING</li>
    <li>EVENTS</li>
    <li>ABOUT US</li>
    <li>CONTACT</li>
  </ul>
</nav>

<section class="hero" role="img" aria-label="Bright kitchen and dining area with wooden cabinets, red-cushioned chairs and large windows">
  <div class="hero-caption">ROOM RENTAL STARTING AT <b>2500</b><sub>/month</sub></div>
  <svg class="hero-arrows" width="18" height="12" viewBox="0 0 18 12" aria-hidden="true"><path d="M6 1L1 6l5 5M12 1l5 5-5 5" fill="none" stroke="#fff" stroke-width="1.4"/></svg>
</section>

<section class="welcome">
  <h1 class="heading">Welcome to <span>Harbor Nest Lodging</span></h1>
  <div class="rule center"></div>
  <p>Traditional apartments and housing rentals are a thing of the past. We have created an all-encompassing living experience that aligns perfectly with your trendy, yet sophisticated lifestyle. Harbor Nest Lodging is unlike anything you have ever experienced before. We invite you to explore our selection of home communities and discover the passion we have for providing wonderful experiencesSed ut perspiciatis unde omnis iste natus error sit voluptatem accusantium doloremque laudantium, totam rem aperiam, eaque ipsa quae ab illo inventore veritatis et quasi architecto beatae vitae dicta sunt</p>
  <span class="btn-primary">CONTACT US</span>
</section>

<section class="amenities">
  <div class="photo" role="img" aria-label="Furnished bedroom with upholstered headboard, lamps and soft blue curtains"></div>
  <h2>LUXURIOUS AMENITIES<sup>*</sup></h2>
  <div class="rule"></div>
  <ul class="list-a">
    <li><svg width="7" height="7" viewBox="0 0 7 7" aria-hidden="true"><circle cx="3.5" cy="3.5" r="3.5" fill="#fff"/><path d="M3 2l1.5 1.5L3 5" fill="none" stroke="#1565c0" stroke-width="1"/></svg>High-speed Wi-Fi</li>
    <li><svg width="7" height="7" viewBox="0 0 7 7" aria-hidden="true"><circle cx="3.5" cy="3.5" r="3.5" fill="#fff"/><path d="M3 2l1.5 1.5L3 5" fill="none" stroke="#1565c0" stroke-width="1"/></svg>All inclusive utilities (with Green Cap)</li>
    <li><svg width="7" height="7" viewBox="0 0 7 7" aria-hidden="true"><circle cx="3.5" cy="3.5" r="3.5" fill="#fff"/><path d="M3 2l1.5 1.5L3 5" fill="none" stroke="#1565c0" stroke-width="1"/></svg>Optional enclosed garage</li>
    <li><svg width="7" height="7" viewBox="0 0 7 7" aria-hidden="true"><circle cx="3.5" cy="3.5" r="3.5" fill="#fff"/><path d="M3 2l1.5 1.5L3 5" fill="none" stroke="#1565c0" stroke-width="1"/></svg>Fully furnished kitchen</li>
    <li><svg width="7" height="7" viewBox="0 0 7 7" aria-hidden="true"><circle cx="3.5" cy="3.5" r="3.5" fill="#fff"/><path d="M3 2l1.5 1.5L3 5" fill="none" stroke="#1565c0" stroke-width="1"/></svg>Washer and dryer</li>
    <li><svg width="7" height="7" viewBox="0 0 7 7" aria-hidden="true"><circle cx="3.5" cy="3.5" r="3.5" fill="#fff"/><path d="M3 2l1.5 1.5L3 5" fill="none" stroke="#1565c0" stroke-width="1"/></svg>Spacious, newly updated rooms</li>
  </ul>
  <ul class="list-b">
    <li><svg width="7" height="7" viewBox="0 0 7 7" aria-hidden="true"><circle cx="3.5" cy="3.5" r="3.5" fill="#fff"/><path d="M3 2l1.5 1.5L3 5" fill="none" stroke="#1565c0" stroke-width="1"/></svg>Private use, full bath with each room</li>
    <li><svg width="7" height="7" viewBox="0 0 7 7" aria-hidden="true"><circle cx="3.5" cy="3.5" r="3.5" fill="#fff"/><path d="M3 2l1.5 1.5L3 5" fill="none" stroke="#1565c0" stroke-width="1"/></svg>Bi-monthly community events</li>
    <li><svg width="7" height="7" viewBox="0 0 7 7" aria-hidden="true"><circle cx="3.5" cy="3.5" r="3.5" fill="#fff"/><path d="M3 2l1.5 1.5L3 5" fill="none" stroke="#1565c0" stroke-width="1"/></svg><span>Various networking event invitations, well suited&nbsp; for young professionals</span></li>
  </ul>
</section>

<section class="features">
  <article class="feature">
    <h3 class="heading">Home <span>with HNL</span></h3>
    <div class="rule"></div>
    <div class="thumb thumb-home" role="img" aria-label="Sunny living room with rug, sofa and large windows"></div>
    <p>Sedperspiciatis unde omnis iste natus error sit voltatem accusantium doloremque laudantium, totam rem aperiam, eaque ipsa quae ab illo inventore veritatis et quasi architecto beatae vitae dicta sSedperspias und omnis iste natus error sit voluptatem accusan</p>
    <span class="btn-small">READ MORE <svg width="6" height="6" viewBox="0 0 6 6" aria-hidden="true"><circle cx="3" cy="3" r="3" fill="#fff"/><path d="M2.5 1.7L3.8 3 2.5 4.3" fill="none" stroke="#1565c0" stroke-width=".9"/></svg></span>
  </article>
  <article class="feature">
    <h3 class="heading">Most <span>Recent Events</span></h3>
    <div class="rule"></div>
    <div class="thumb thumb-events" role="img" aria-label="Group of friends laughing together on a sofa at a house party"></div>
    <p>Sedperspiciatis unde omnis iste natus error sit voltatem accusantium doloremque laudantium, totam rem aperiam, eaque ipsa quae ab illo inventore veritatis et quasi architecto beatae vitae dicta sSedperspias und omnis iste natus error sit voluptatem accusan</p>
    <span class="btn-small">READ MORE <svg width="6" height="6" viewBox="0 0 6 6" aria-hidden="true"><circle cx="3" cy="3" r="3" fill="#fff"/><path d="M2.5 1.7L3.8 3 2.5 4.3" fill="none" stroke="#1565c0" stroke-width=".9"/></svg></span>
  </article>
  <article class="feature">
    <h3 class="heading">Our <span>Latest Addition</span></h3>
    <div class="rule"></div>
    <div class="thumb thumb-addition" role="img" aria-label="Newly furnished bedroom with blue bedspread and wooden headboard"></div>
    <p>Sedperspiciatis unde omnis iste natus error sit voltatem accusantium doloremque laudantium, totam rem aperiam, eaque ipsa quae ab illo inventore veritatis et quasi architecto beatae vitae dicta sSedperspias und omnis iste natus error sit voluptatem accusan</p>
    <span class="btn-small">READ MORE <svg width="6" height="6" viewBox="0 0 6 6" aria-hidden="true"><circle cx="3" cy="3" r="3" fill="#fff"/><path d="M2.5 1.7L3.8 3 2.5 4.3" fill="none" stroke="#1565c0" stroke-width=".9"/></svg></span>
  </article>
</section>

<section class="fans">
  <h2 class="heading">Our <span>Fans</span></h2>
  <div class="rule center"></div>
  <div class="fan fan-a">
    <div class="avatar avatar-a" role="img" aria-label="Portrait photo of resident Dale"></div>
    <blockquote>I thought I wanted to live on my own, but the reality is I just didn't want to go through the hassle of finding a good room mate. Someone with common interests that's not out partying al night. I'm a professional and don't need that in my life. Now I'm a part of a great social, athletic, professional community that encourages the most out of me.</blockquote>
    <div class="name">Dale, 30</div>
  </div>
  <div class="fan fan-b">
    <div class="avatar avatar-b" role="img" aria-label="Portrait photo of resident Marisa"></div>
    <blockquote>People are social creatures. It's simply a human trait. Whether we are introverts or extroverts, shy or gregarious, we need to know that we are part of a common group. We need to feel that we have others with whom we connect and who share commonalities. I love feeling accepted as a piece of a greater puzzle where we look out for each other, support each other's needs.</blockquote>
    <div class="name">Marisa,</div>
  </div>
</section>

<footer class="footer">
  <div class="brand-foot">Harbor Nest Lodging</div>
  <address>harbornestlodging.example&nbsp; 18 Quayside Row<br>Portvale TX 70000<br>Tel: 555-014-2278&nbsp; Email: hello@harbornest.example</address>
  <div class="social" aria-label="Social links">
    <span title="chirpnet"></span><span title="vidloop"></span><span title="friendbook"></span><span title="workline"></span>
  </div>
  <div class="copy">Copyright © 2016&nbsp; All Rights Reserved. Harbor Nest Lodging.example</div>
</footer>

</body>
</html>
```